Robotic startup business cards

We are looking for a design for a set of business cards which reflect the spirit and humor of Vortalo Robotics. We want to present ourselves as sleek, professional, but laid-back consulting company.

We primarily focus on developing robotic arms software. This software controls robots and does things like grab items, pick objects up, move them, etc.

We want to allow you maximum design creativity, but do ask that you consider our existing style guidelines (see attached files) in order to make our brand cohesive.

Target Market(s)

Startups and Mid-size robotic companies

Industry/Entity Type

Business

Contact Information for Business Card

Miro Halvensky, PhD
Roboticist | Vortalo Consulting | 318.570.9164

Font styles to use
Other font styles liked:
• Source code pro

Requirements
Must have
• robots or robotic arms
• similar color scheme that works with existing brand guidelines
Nice to have
• please consider our existing style guidelines (see attached files) in order to make our brand cohesive.
• minimalism style is generally nice.
Should not have
• An old, boring, or corporate feel. Too much text.

```html
<!DOCTYPE html>
<html lang="en">
<head>
<meta charset="UTF-8">
<title>Vortalo Robotics — Business Cards</title>
<link rel="stylesheet" href="https://fonts.googleapis.com/css2?family=Source+Code+Pro:wght@500&family=Source+Sans+3:wght@400&display=swap">
<style>
  :root {
    --backdrop: #b9b9b9;
    --card-dark-top: #3c3d42;
    --card-dark-bottom: #2f3034;
    --card-green-top: #05d892;
    --card-green-bottom: #01c184;
    --accent: #05d48f;
    --text-light: #e8e9ea;
    --text-muted: #cfd1d3;
    --ink: #2f3034;
  }
  * { margin: 0; padding: 0; box-sizing: border-box; }
  html, body {
    width: 1200px;
    height: 576px;
    overflow: hidden;
    background: var(--backdrop);
  }
  .canvas {
    position: relative;
    width: 1200px;
    height: 576px;
  }
  .card {
    position: absolute;
    top: 139px;
    width: 484px;
    height: 291px;
    border-radius: 13px;
    box-shadow: 0 3px 6px rgba(0, 0, 0, 0.25);
    overflow: hidden;
  }
  .card--front {
    left: 82px;
    background: linear-gradient(180deg, var(--card-dark-top), var(--card-dark-bottom));
  }
  .card--back {
    left: 602px;
    background: linear-gradient(180deg, var(--card-green-top), var(--card-green-bottom));
  }
  .contact {
    position: absolute;
    left: 35px;
    top: 37px;
    font-family: "Source Sans 3", sans-serif;
    color: var(--text-light);
  }
  .contact__name {
    font-size: 20px;
    font-weight: 400;
    line-height: 1.2;
  }
  .contact__role {
    margin-top: 3px;
    font-size: 12px;
    color: var(--text-muted);
  }
  .contact__details {
    margin-top: 18px;
    list-style: none;
    font-size: 12px;
    line-height: 16.5px;
    color: var(--text-light);
  }
  .contact__highlight { color: var(--accent); }
  .brand {
    position: absolute;
    display: flex;
    align-items: center;
    gap: 17px;
  }
  .card--front .brand { left: 35px; top: 211px; }
  .card--back .brand { left: 259px; top: 210px; }
  .brand__dot {
    width: 40px;
    height: 40px;
    border-radius: 50%;
  }
  .card--front .brand__dot { background: var(--accent); }
  .card--back .brand__dot { background: var(--ink); }
  .brand__name {
    font-family: "Source Code Pro", monospace;
    font-weight: 500;
    font-size: 23px;
    letter-spacing: 4px;
  }
  .card--front .brand__name { color: var(--text-light); }
  .card--back .brand__name { color: var(--ink); }
</style>
</head>
<body>
<main class="canvas">
  <section class="card card--front" aria-label="Business card front">
    <div class="contact">
      <h1 class="contact__name">Miro Halvensky, PhD</h1>
      <p class="contact__role">Roboticist | Vortalo Consulting</p>
      <ul class="contact__details">
        <li>318.570.9164</li>
        <li>miro@vortalo.com</li>
        <li>www.<span class="contact__highlight">vortalo</span>.com</li>
      </ul>
    </div>
    <div class="brand">
      <span class="brand__dot" aria-hidden="true"></span>
      <span class="brand__name">VORTALO</span>
    </div>
  </section>

  <section class="card card--back" aria-label="Business card back">
    <div class="brand">
      <span class="brand__dot" aria-hidden="true"></span>
      <span class="brand__name">VORTALO</span>
    </div>
  </section>
</main>
</body>
</html>
```